Pell Tor Website

Need a website that will highlight our product and provide a storefront for purchases. The design of the site (colors, logo, theme) needs to closely match the design of the product packaging and I am including files and ai file of this packaging.

Target Market(s)

Males and Females aged 16-70.

Number of Pages Required

4 page

Font styles to use
Serif

Requirements
Must have
• Home page, Product Page, Contact us page, Shop Page
• Use the general design theme that is shown in the attached AI file. Must have Pell Tor logo, must have pictures of the bugs as shown in the packaging. Can use all of the information on the ai file.
Nice to have
• Bold, clear, clean.

```html
<!DOCTYPE html>
<html lang="en">
<head>
<meta charset="utf-8">
<title>Pell Tor – Home</title>
<link href="https://fonts.googleapis.com/css2?family=Oswald:wght@500;600&family=Roboto:wght@400;500;700;900&display=swap" rel="stylesheet">
<style>
:root{
  --red:#c4161c;
  --orange:#f7a326;
  --ink:#222222;
  --text:#555555;
  --muted:#8a8a8a;
  --panel:#ececec;
  --line:#dddddd;
  --footer:#2b2b2b;
  --footer-bottom:#1e1e1e;
  --white:#ffffff;
}
*{box-sizing:border-box;margin:0;padding:0}
html,body{width:1200px;height:4898px;overflow:hidden}
body{position:relative;background:var(--white);font-family:'Roboto',sans-serif;color:var(--text)}
.abs{position:absolute}
a{color:inherit;text-decoration:none}

/* top bar */
.topbar{left:0;top:0;width:1200px;height:33px;background:var(--ink);color:#fff;font-size:12px;font-weight:500}
.topbar .call{left:143px;top:9px}
.topbar .account{left:762px;top:9px}
.topbar .social{left:1003px;top:11px;display:flex;gap:6px}
.topbar .social span{width:10px;height:10px;border-radius:50%;background:#fff}

/* header */
.brand{left:143px;top:48px;width:152px;height:108px;display:flex;align-items:center;gap:8px}
.brand .dot{width:14px;height:14px;background:var(--red);border-radius:50%}
.brand b{font-size:24px;font-weight:900;color:var(--ink)}
.search{left:588px;top:58px;width:347px;height:40px;border:1px solid #cfcfcf;font-size:12px;color:var(--muted);padding:12px 14px}
.search svg{position:absolute;right:12px;top:13px}
.icon-user{left:958px;top:62px}
.icon-cart{left:1014px;top:62px}
.nav{left:385px;top:127px;display:flex;gap:28px;font-size:15px;font-weight:500;color:var(--ink)}
.nav .active{color:var(--red);position:relative}
.nav .active::after{content:"";position:absolute;left:-4px;right:-4px;top:36px;height:3px;background:var(--red)}

/* hero */
.hero{left:0;top:168px;width:1200px;height:627px;background:linear-gradient(90deg,#1b130d 0%,#2e2016 40%,#5a3f2a 70%,#33241a 100%)}
.hero h1{left:141px;top:120px;font-family:'Oswald',sans-serif;font-weight:500;font-size:44px;line-height:52px;color:#fff;text-transform:uppercase}
.hero ul{left:143px;top:242px;list-style:none;font-family:'Oswald',sans-serif;font-size:15px;color:#fff}
.hero li{height:28px;display:flex;align-items:center;gap:12px}
.hero li::before{content:"";width:12px;height:12px;border-radius:50%;background:#f5d800}
.btn{display:inline-flex;align-items:center;justify-content:center;background:var(--red);color:#fff;font-weight:700;font-size:13px;text-transform:uppercase}
.hero .btn{left:143px;top:412px;width:134px;height:35px}
.arrow{width:40px;height:40px;border:1.5px solid rgba(255,255,255,.8);border-radius:50%;display:flex;align-items:center;justify-content:center}
.hero .arrow.prev{left:47px;top:317px}
.hero .arrow.next{left:1111px;top:317px}

/* services */
.packshot{left:143px;top:742px;width:522px;height:327px;background:linear-gradient(135deg,#f6d21a 0%,#e88a1c 45%,#c4161c 100%)}
.service{width:179px;height:158px;color:#fff;text-align:center;padding-top:34px}
.service h3{font-size:14px;font-weight:700;text-transform:uppercase;margin-top:14px}
.service p{font-size:12px;margin-top:6px;line-height:18px;opacity:.9}
.service.orange{background:var(--orange)}
.service.red{background:var(--red)}

/* welcome */
.welcome{left:143px;top:1160px;width:912px;height:396px;background:var(--panel)}
.welcome h2{left:34px;top:62px;font-size:36px;font-weight:400;color:var(--ink)}
.welcome h2 b{color:var(--red);font-weight:700}
.rule{width:60px;height:3px;background:var(--red)}
.welcome .rule{left:34px;top:115px}
.welcome p{left:34px;top:136px;width:435px;font-size:13px;line-height:24px}
.outline-btn{left:34px;top:308px;width:161px;height:41px;border:2px solid var(--red);color:var(--red);font-size:13px;font-weight:700;display:flex;align-items:center;justify-content:center}
.brand-mark{left:520px;width:392px;height:396px;display:flex;align-items:center;justify-content:center;gap:10px}
.brand-mark .dot{width:18px;height:18px;border-radius:50%;background:var(--red)}
.brand-mark b{font-size:34px;font-weight:900;color:var(--ink)}

/* categories */
.tile{width:597px;height:371px}
.tile h3{font-size:28px;font-weight:700;line-height:36px;text-transform:uppercase;color:var(--ink)}
.tile .btn{width:120px;height:36px}

/* featured */
.section-title{left:0;width:1200px;text-align:center;font-size:38px;font-weight:700;color:var(--ink);text-transform:uppercase}
.section-rule{left:570px;width:60px;height:3px;background:var(--red)}
.card{width:212px;height:380px;border:1px solid var(--line);text-align:center}
.card .shot{margin:8px;height:210px}
.card h4{font-size:13px;font-weight:500;color:#333;line-height:21px;margin-top:12px;text-transform:uppercase}
.card .price{margin-top:10px;font-size:14px}
.card .price s{color:#777;margin-right:8px}
.card .price b{color:var(--red);font-weight:500}
.card .btn{margin-top:18px;width:128px;height:34px;border-radius:17px;font-size:12px}
.round-arrow{width:36px;height:36px;border:1.5px solid #777;border-radius:50%;display:flex;align-items:center;justify-content:center}

/* newsletter */
.newsletter{left:143px;top:3094px;width:912px;height:395px;background:var(--panel)}
.newsletter h2{left:49px;top:66px;font-size:38px;font-weight:700;line-height:44px;color:var(--ink);text-transform:uppercase;letter-spacing:1px}
.newsletter p{left:49px;top:167px;width:360px;font-size:15px;line-height:24px;color:#333}
.newsletter .field{left:49px;top:226px;width:336px;height:38px;border-radius:19px;background:#fff;border:1px solid var(--line);font-size:11px;color:var(--muted);padding:12px 16px}
.newsletter .btn{left:49px;top:286px;width:138px;height:37px;border-radius:19px}

/* blog */
.post{width:288px;text-align:center}
.post .shot{height:188px}
.post .date{width:50px;height:50px;border-radius:50%;background:var(--red);border:3px solid #fff;margin:-25px auto 0;position:relative;color:#fff;font-size:20px;font-weight:700;line-height:20px;padding-top:7px}
.post .date small{display:block;font-size:8px;line-height:9px}
.post p{margin-top:12px;font-size:15px;line-height:24px;color:#444}

/* brands */
.brands{left:0;top:4046px;width:1200px;height:348px;background:var(--orange)}
.brands h2{left:0;top:54px;width:1200px;text-align:center;color:#fff;font-size:36px;font-weight:700}
.brands .section-rule{top:106px;background:#fff}
.logo-box{top:166px;width:138px;height:81px;background:#fff;display:flex;align-items:center;justify-content:center;gap:6px;font-size:17px;font-weight:700;color:#333}
.logo-box i{width:10px;height:10px;background:#333;display:block}

/* footer */
.footer{left:0;top:4394px;width:1200px;height:504px;background:var(--footer);color:#d0d0d0}
.footer h5{font-size:17px;font-weight:700;color:#fff;text-transform:uppercase}
.footer .contact-line{display:flex;gap:14px;font-size:14px;line-height:20px;color:#d0d0d0}
.footer ul{list-style:none;font-size:13.5px;line-height:29px}
.footer ul li::before{content:"›";margin-right:10px}
.footer .brand-foot{left:892px;top:96px;display:flex;align-items:center;gap:8px}
.footer .brand-foot .dot{width:14px;height:14px;border-radius:50%;background:var(--red)}
.footer .brand-foot b{font-size:26px;font-weight:900;color:#fff}
.footer .bottom{left:0;top:398px;width:1200px;height:106px;background:var(--footer-bottom);text-align:center;font-size:13px;padding-top:47px}
.pay{width:44px;height:28px;border-radius:3px}
.soc{width:30px;height:30px;border:2px solid #fff;border-radius:50%}
</style>
</head>
<body>

<div class="abs topbar">
  <span class="abs call">&#9990; CALL US : 555 0140 2020</span>
  <span class="abs account">&#9679; My Account &nbsp;&nbsp;|&nbsp;&nbsp; &#9829; My Wishlist</span>
  <span class="abs social"><span></span><span></span><span></span></span>
</div>

<div class="abs brand"><span class="dot"></span><b>Pell Tor</b></div>
<div class="abs search">Search products...
  <svg width="12" height="12" viewBox="0 0 12 12"><circle cx="5" cy="5" r="4" fill="none" stroke="#333" stroke-width="1.6"/><path d="M8 8l3 3" stroke="#333" stroke-width="1.6"/></svg>
</div>
<svg class="abs icon-user" width="32" height="32" viewBox="0 0 32 32"><circle cx="16" cy="10" r="7" fill="none" stroke="#c4161c" stroke-width="2"/><path d="M3 30c1-8 6-12 13-12s12 4 13 12z" fill="none" stroke="#c4161c" stroke-width="2"/></svg>
<svg class="abs icon-cart" width="40" height="34" viewBox="0 0 40 34"><path d="M2 6h6l4 17h18l4-13H10" fill="none" stroke="#c4161c" stroke-width="2"/><circle cx="14" cy="29" r="2.5" fill="#c4161c"/><circle cx="28" cy="29" r="2.5" fill="#c4161c"/><circle cx="33" cy="5" r="5" fill="#666"/><text x="33" y="8" font-size="7" fill="#fff" text-anchor="middle" font-family="Roboto,sans-serif">0</text></svg>
<nav class="abs nav">
  <a class="active">HOME</a><a>ABOUT US</a><a>OUR PRODUCTS</a><a>SHOP</a><a>PACKAGING</a><a>BLOG</a><a>CONTACT US</a>
</nav>

<section class="abs hero" role="img" aria-label="Cowboy hat resting on worn leather boots in a dark wooden barn">
  <h1 class="abs">Package contains<br>one pair (2pcs)</h1>
  <ul class="abs">
    <li>Durable poly blend covers</li>
    <li>Reusable</li>
    <li>One size fits all</li>
    <li>Machine washable</li>
    <li>Secure elastic prevents intruders</li>
  </ul>
  <a class="abs btn">Shop now</a>
  <span class="abs arrow prev"><svg width="12" height="18"><path d="M10 2L3 9l7 7" fill="none" stroke="#fff" stroke-width="1.6"/></svg></span>
  <span class="abs arrow next"><svg width="12" height="18"><path d="M2 2l7 7-7 7" fill="none" stroke="#fff" stroke-width="1.6"/></svg></span>
</section>

<div class="abs packshot" role="img" aria-label="Product packaging: yellow and red card with boot cover and pest icons"></div>
<div class="abs service orange" style="left:681px;top:742px">
  <svg width="40" height="32" viewBox="0 0 40 32"><path d="M3 6h22v18H3zM25 12h8l5 6v6H25" fill="none" stroke="#fff" stroke-width="1.6"/><circle cx="11" cy="26" r="3" fill="none" stroke="#fff" stroke-width="1.6"/><circle cx="31" cy="26" r="3" fill="none" stroke="#fff" stroke-width="1.6"/></svg>
  <h3>Free returns</h3><p>Duis aute irure dolor in</p>
</div>
<div class="abs service red" style="left:875px;top:742px">
  <svg width="36" height="34" viewBox="0 0 36 34"><path d="M5 20v-4a13 13 0 0 1 26 0v4" fill="none" stroke="#fff" stroke-width="2"/><rect x="3" y="18" width="7" height="11" rx="2" fill="none" stroke="#fff" stroke-width="2"/><rect x="26" y="18" width="7" height="11" rx="2" fill="none" stroke="#fff" stroke-width="2"/></svg>
  <h3>Online support</h3><p>Lorem ipsum dolor</p>
</div>
<div class="abs service red" style="left:681px;top:909px;padding-top:26px">
  <svg width="36" height="36" viewBox="0 0 36 36"><circle cx="18" cy="18" r="15" fill="none" stroke="#fff" stroke-width="3"/><path d="M18 9v10h7" fill="none" stroke="#fff" stroke-width="3"/></svg>
  <h3>48 hrs shipping</h3><p>V / booking before<br>kl. 16.30 Mon-Fri</p>
</div>
<div class="abs service orange" style="left:875px;top:909px">
  <svg width="44" height="32" viewBox="0 0 44 32"><rect x="3" y="5" width="38" height="22" rx="3" fill="none" stroke="#fff" stroke-width="1.6"/><circle cx="22" cy="16" r="6" fill="none" stroke="#fff" stroke-width="1.6"/></svg>
  <h3>Easy payment</h3><p>For purchases from 499</p>
</div>

<section class="abs welcome">
  <h2 class="abs">Welcome to <b>Pell Tor</b></h2>
  <span class="abs rule"></span>
  <p class="abs">Lorem ipsum dolor sit ameconsectetur adipiscing eli do eiusmod tempor incididuntbore et dolore magna aliquaeis ipsum suspendisse ultrices gravida. Risus commodo viverra maecenasaccumsan lacus vel facilore ore et dolore magna aliquauis ipsum suspendisse ultrices gravet dolore magna aliore et dolore magna alis ipsum suspendisse ultrices gravquaum suspendisse ultrices gravisis.</p>
  <a class="abs outline-btn">READ MORE</a>
  <div class="abs brand-mark" style="top:0"><span class="dot"></span><b>Pell Tor</b></div>
</section>

<div class="abs tile" style="left:0;top:1658px;background:linear-gradient(90deg,#8a5a34,#c9b9a3 60%,#d9d2c6)" role="img" aria-label="Brown leather cowboy boots with a hat against grey planks">
  <h3 class="abs" style="left:320px;top:136px">Nemo enim ipsam<br>voluptatem</h3>
  <a class="abs btn" style="left:320px;top:222px">Shop now</a>
</div>
<div class="abs tile" style="left:603px;top:1658px;background:linear-gradient(90deg,#d8d6d3,#efeeec 55%,#9d9994)" role="img" aria-label="Woman walking in ankle boots with a black handbag">
  <h3 class="abs" style="left:42px;top:136px">Nemo enim ipsam<br>voluptatem</h3>
  <a class="abs btn" style="left:42px;top:234px">Shop now</a>
</div>
<div class="abs tile" style="left:0;top:2035px;background:linear-gradient(180deg,#e7c98c,#d8a55c 55%,#6b5035)" role="img" aria-label="Worn cowboy boots and hat in a sunset field with riders">
  <h3 class="abs" style="left:300px;top:40px;text-align:center">Nemo enim ipsam<br>voluptatem</h3>
  <a class="abs btn" style="left:370px;top:122px">Shop now</a>
</div>
<div class="abs tile" style="left:603px;top:2035px;background:linear-gradient(135deg,#e09a3a,#a7562a 50%,#4a2c1c)" role="img" aria-label="Brown leather boot stepping on autumn leaves">
  <h3 class="abs" style="left:42px;top:115px;color:#fff">Nemo enim ipsam<br>voluptatem</h3>
  <a class="abs btn" style="left:42px;top:209px">Shop now</a>
</div>

<h2 class="abs section-title" style="top:2492px">Featured products</h2>
<span class="abs section-rule" style="top:2558px"></span>
<span class="abs round-arrow" style="left:73px;top:2779px"><svg width="10" height="14"><path d="M8 2L3 7l5 5" fill="none" stroke="#555" stroke-width="1.5"/></svg></span>
<span class="abs round-arrow" style="left:1091px;top:2779px"><svg width="10" height="14"><path d="M2 2l5 5-5 5" fill="none" stroke="#555" stroke-width="1.5"/></svg></span>
<div class="abs card" style="left:143px;top:2609px"><div class="shot" style="background:linear-gradient(180deg,#a9c6e3,#8c6040)" role="img" aria-label="Boot with brown hat against blue sky"></div><h4>Nemo enim ipsam<br>voluptatem quia volu</h4><div class="price"><s>$95.00</s><b>$75.00</b></div><a class="btn">Add to cart</a></div>
<div class="abs card" style="left:378px;top:2609px"><div class="shot" style="background:linear-gradient(180deg,#d9d0c4,#7a5c44)" role="img" aria-label="Worn boot with hat on a pale background"></div><h4>Nemo enim ipsam<br>voluptatem quia volu</h4><div class="price"><s>$95.00</s><b>$75.00</b></div><a class="btn">Add to cart</a></div>
<div class="abs card" style="left:612px;top:2609px"><div class="shot" style="background:linear-gradient(180deg,#6b5846,#c9c4bd 45%,#3a2d23)" role="img" aria-label="White hat on a dark boot on wooden boards"></div><h4>Nemo enim ipsam<br>voluptatem quia volu</h4><div class="price"><s>$95.00</s><b>$75.00</b></div><a class="btn">Add to cart</a></div>
<div class="abs card" style="left:846px;top:2609px"><div class="shot" style="background:linear-gradient(180deg,#c9b9a6,#6d4f37)" role="img" aria-label="Brown hat on a leather boot"></div><h4>Nemo enim ipsam<br>voluptatem quia volu</h4><div class="price"><s>$95.00</s><b>$75.00</b></div><a class="btn">Add to cart</a></div>

<section class="abs newsletter">
  <h2 class="abs">Join our<br>newsletter</h2>
  <p class="abs">Subscribe to our mailing list to receive updates and promotional offers.</p>
  <div class="abs field">Enter your E – mail</div>
  <a class="abs btn">Subscribe</a>
  <div class="abs brand-mark" style="top:0"><span class="dot"></span><b>Pell Tor</b></div>
</section>

<h2 class="abs section-title" style="top:3564px">Latest blog</h2>
<span class="abs section-rule" style="top:3628px"></span>
<article class="abs post" style="left:143px;top:3676px"><div class="shot" style="background:linear-gradient(90deg,#5e5e5e,#9a9a9a 60%,#d5d5d5)" role="img" aria-label="Woman in fur coat and boots sitting on steps"></div><div class="date">02<small>FEB</small></div><p>Nemo enim ipsam voluptatem quia voluptas sit aspernatur</p></article>
<article class="abs post" style="left:454px;top:3676px"><div class="shot" style="background:linear-gradient(180deg,#8fa3c4,#5a6478 55%,#3d3b3a)" role="img" aria-label="Woman resting in hiking boots on a mountain"></div><div class="date">02<small>FEB</small></div><p>Nemo enim ipsam voluptatem quia voluptas sit aspernatur</p></article>
<article class="abs post" style="left:766px;top:3676px"><div class="shot" style="background:linear-gradient(90deg,#f0f0f0,#5b5f6b 50%,#e6e6e6)" role="img" aria-label="Person in dark tall boots on a white floor"></div><div class="date">02<small>FEB</small></div><p>Nemo enim ipsam voluptatem quia voluptas sit aspernatur</p></article>

<section class="abs brands">
  <h2 class="abs">OUR BRAND</h2>
  <span class="abs section-rule"></span>
  <svg class="abs" style="left:110px;top:196px" width="12" height="20"><path d="M10 2L3 10l7 8" fill="none" stroke="#333" stroke-width="2"/></svg>
  <svg class="abs" style="left:1074px;top:196px" width="12" height="20"><path d="M2 2l7 8-7 8" fill="none" stroke="#333" stroke-width="2"/></svg>
  <div class="abs logo-box" style="left:143px"><i></i>KESTREL</div>
  <div class="abs logo-box" style="left:298px">Orvane</div>
  <div class="abs logo-box" style="left:453px"><i></i>TALLOW</div>
  <div class="abs logo-box" style="left:608px">Merrin</div>
  <div class="abs logo-box" style="left:764px"><i></i>Quillway</div>
  <div class="abs logo-box" style="left:920px">Bramble</div>
</section>

<footer class="abs footer">
  <h5 class="abs" style="left:118px;top:82px">Contact us</h5>
  <div class="abs" style="left:118px;top:128px;display:flex;flex-direction:column;gap:10px">
    <div class="contact-line"><svg width="16" height="20" viewBox="0 0 16 20"><path d="M8 19s-6-7-6-11a6 6 0 0 1 12 0c0 4-6 11-6 11z" fill="#fff"/><circle cx="8" cy="8" r="2.2" fill="#2b2b2b"/></svg><span>ADDRESS<br>48 Harrow Lane, Millbrook, England</span></div>
    <div class="contact-line"><svg width="16" height="16" viewBox="0 0 16 16"><path d="M3 1l3 1 1 3-2 2a9 9 0 0 0 4 4l2-2 3 1 1 3-2 2C6 15 1 10 1 3z" fill="#fff"/></svg><span>Phone: (555) 014-7721</span></div>
    <div class="contact-line"><svg width="16" height="14" viewBox="0 0 16 14"><rect x="1" y="2" width="14" height="10" fill="#fff"/><path d="M1 2l7 6 7-6" fill="none" stroke="#2b2b2b" stroke-width="1.2"/></svg><span>E-mail: info@pelltor.com</span></div>
    <div class="contact-line"><svg width="16" height="16" viewBox="0 0 16 16"><circle cx="8" cy="8" r="7" fill="#fff"/><path d="M8 4v4h3" fill="none" stroke="#2b2b2b" stroke-width="1.5"/></svg><span>Opening hours:<br><small style="font-size:13px">Man-Thurs: 9.30-17.30<br>Fri: 9.30-18.00</small></span></div>
  </div>
  <h5 class="abs" style="left:416px;top:82px">Information</h5>
  <ul class="abs" style="left:416px;top:118px"><li>Product Warranty</li><li>Pell Tor</li><li>Disclaimer</li><li>Terms of Use</li><li>Privacy Policy</li></ul>
  <h5 class="abs" style="left:648px;top:82px">My account</h5>
  <ul class="abs" style="left:648px;top:118px"><li>Terms &amp; Conditions</li><li>Privacy Policy</li><li>Right of Refusal &amp; Returns</li><li>Cookies</li><li>Shipping &amp; Delivery Terms</li></ul>
  <div class="abs brand-foot"><span class="dot"></span><b>Pell Tor</b></div>
  <div class="abs" style="left:892px;top:180px;display:flex;gap:6px">
    <span class="pay" style="background:#e8e8e8"></span><span class="pay" style="background:#d9d9d9"></span><span class="pay" style="background:#e8e8e8"></span><span class="pay" style="background:#d9d9d9"></span>
  </div>
  <div class="abs" style="left:970px;top:226px;display:flex;gap:10px"><span class="soc"></span><span class="soc"></span><span class="soc"></span></div>
  <div class="abs bottom">© 2020 Pell Tor. All Rights Reserved.</div>
</footer>

</body>
</html>
```